Noche de Salsa

We need a poster to promote a party. It is a salsa night at La Tortuga, a fun night out to dance, be with friends and have a few drinks. It is an informal occasion. The drinks will not be expensive and the snack will be typical mexican food.
La Tortuga is a campus for 8 local non-profit organizations but it also has high quality event venues and outdoor areas.
We would like a file for print (11x17") and a digital file for social media.
Enclosed:
- File with poster contents in spanish.
- La Tortuga logo
- Picture of palm trees at La Tortuga (you don't have to include this if another graphic fits best.
- Pic of the outside of the restaurant, where the dancing will take place. The restaurante is right in fron of the beach. THIS PICTURE DOES NOT NECESSARILY NEEDS TO BE PART OF THE POSTER.
- La Tortuga Fact Sheet for context.
Target Market(s)
Men and women from 25 to 50 years old.
American and mexican citizens.
Industry/Entity Type
Non-Profit
Colors
Designer to choose colors to be used in the design.
Look and feel
Each slider illustrates characteristics of the customer's brand and the style your logo design should communicate.

```html
<!DOCTYPE html>
<html lang="es">
<head>
<meta charset="utf-8">
<title>Noche de Salsa – La Tortuga</title>
<link href="https://fonts.googleapis.com/css2?family=Kaushan+Script&family=Oswald:wght@400&family=Raleway:wght@500&family=Roboto:wght@400;700&display=swap" rel="stylesheet">
<style>
  :root {
    --night-deep: #1a1533;
    --night-mid: #241d45;
    --night-violet: #3b1d4a;
    --moon-core: #8f96dc;
    --moon-blue: #5a6fc0;
    --moon-haze: rgba(70, 60, 140, .55);
    --star-warm: rgba(230, 130, 60, .28);
    --magenta: #c92f7e;
    --orange: #f2a23c;
    --gold: #e7a236;
    --lime: #d9e43a;
    --lavender: #a39bd3;
    --band: #a3195f;
    --white: #ffffff;
  }
  * { margin: 0; padding: 0; box-sizing: border-box; }
  html, body { width: 856px; height: 1200px; overflow: hidden; background: #ececec; }
  .poster {
    position: relative;
    width: 856px; height: 1200px;
    overflow: hidden;
    background:
      radial-gradient(ellipse 60% 40% at 100% 80%, rgba(110,30,90,.55), transparent 70%),
      linear-gradient(180deg, var(--night-mid) 0%, var(--night-deep) 60%, var(--night-violet) 100%);
  }
  .hero-art {
    position: absolute;
    left: 40px; top: 20px;
    width: 780px; height: 560px;
    background:
      radial-gradient(ellipse closest-side at 50% 48%, var(--moon-core) 0%, var(--moon-blue) 38%, var(--moon-haze) 62%, var(--star-warm) 80%, rgba(36,29,69,0) 100%);
  }
  h1 { font-weight: normal; }
  .title {
    position: absolute;
    left: 0; right: 0;
    font-family: "Kaushan Script", cursive;
    text-align: center;
    line-height: 1;
    filter: drop-shadow(3px 4px 0 rgba(10,8,25,.7));
  }
  .title-noche {
    top: 372px;
    font-size: 176px;
    background: linear-gradient(90deg, var(--magenta) 15%, var(--orange) 85%);
    -webkit-background-clip: text; background-clip: text; color: transparent;
  }
  .title-lower { top: 530px; font-size: 128px; padding-left: 50px; }
  .title-de { color: var(--lime); font-size: 76px; vertical-align: 30px; margin-right: 6px; }
  .title-salsa { color: var(--gold); }
  .entry {
    position: absolute; top: 682px; left: 0; right: 0;
    text-align: center;
    font-family: "Raleway", sans-serif; font-weight: 500;
    font-size: 21px; color: var(--white);
  }
  .entry .divider { color: var(--orange); margin: 0 4px; }
  .date {
    position: absolute; top: 722px; left: 0; right: 0;
    text-align: center;
    font-family: "Oswald", sans-serif;
    font-size: 46px; color: var(--gold);
  }
  .venue-photo {
    position: absolute; left: 36px; top: 846px;
    width: 424px; height: 232px;
    background: var(--white);
    padding: 14px 12px 22px;
    transform: rotate(-1.2deg);
    box-shadow: 4px 6px 10px rgba(0,0,0,.5);
  }
  .venue-photo-fill {
    width: 100%; height: 100%;
    background: linear-gradient(180deg, #b9c4b5 0%, #7d8f6a 40%, #b8532e 55%, #cfc8bc 80%, #d8d4cc 100%);
  }
  .brand {
    position: absolute; left: 513px; top: 862px;
    display: flex; align-items: center; gap: 12px;
    font-family: "Roboto", sans-serif; font-weight: 400;
    font-size: 44px; color: var(--white);
  }
  .brand-dot { width: 18px; height: 18px; border-radius: 50%; background: var(--white); }
  .address {
    position: absolute; left: 513px; top: 960px;
    font-family: "Roboto", sans-serif; font-style: normal;
    font-size: 19px; line-height: 26px; color: var(--lavender);
  }
  .info-band {
    position: absolute; left: 0; right: 0; top: 1126px; height: 44px;
    background: var(--band);
    display: flex; align-items: center; justify-content: center;
    font-family: "Roboto", sans-serif; font-weight: 700;
    font-size: 21px; color: var(--white);
  }
</style>
</head>
<body>
  <main class="poster">
    <div class="hero-art" role="img" aria-label="Ilustración: pareja bailando salsa en silueta frente a una luna llena, con palmeras y estrellas"></div>

    <h1>
      <span class="title title-noche">Noche</span>
      <span class="title title-lower"><span class="title-de">de</span><span class="title-salsa">Salsa</span></span>
    </h1>

    <p class="entry">Entrada: $100 pesos <span class="divider">|</span> Incluye 1 bebida.</p>
    <p class="date">Viernes, 14 de noviembre 2014</p>

    <div class="venue-photo">
      <div class="venue-photo-fill" role="img" aria-label="Fotografía del patio del restaurante con palmeras y fachada naranja"></div>
    </div>

    <div class="brand"><span class="brand-dot"></span>La Tortuga</div>

    <address class="address">
      Acceso Costero #1480<br>
      (al final de la calle Palmar<br>
      en la antigua bodega)<br>
      Col. Las Brisas<br>
      C.P. 00000, Puerto Arena, B.C.S.
    </address>

    <div class="info-band">Más informes al 555-0142 / info@latortuga.org</div>
  </main>
</body>
</html>
```